doctor needs a professional business card

please use the attached logo for the design.
Information for the card:
Loretta V Brandwick, MD
4381 Fallow Crest Clinical Way Drive
Wilmington NC 28517
phone 910.586.2741
fax 910.586.2799
practice web site address- brandwickvue.net
Target Market(s)
55 to 80 years old
Industry/Entity Type
Business

```html
<!DOCTYPE html>
<html lang="en">
<head>
<meta charset="utf-8">
<title>Loretta V Brandwick, MD – Business Card</title>
<link rel="stylesheet" href="https://fonts.googleapis.com/css2?family=Jost:wght@300;400&display=swap">
<style>
  :root {
    --panel: #edf2f2;
    --band: #f5f8f8;
    --card: #ffffff;
    --navy: #1b2f86;
    --blue: #2a47a6;
    --icon: #1e3a8f;
  }
  * { margin: 0; padding: 0; box-sizing: border-box; }
  html, body { width: 1200px; height: 704px; overflow: hidden; background: var(--card); }
  .card {
    position: relative;
    width: 1200px;
    height: 704px;
    background: var(--card);
    font-family: "Jost", "Futura", sans-serif;
    font-weight: 300;
    overflow: hidden;
  }
  .brand-panel {
    position: absolute;
    left: 0; top: 0;
    width: 507px; height: 704px;
    background: var(--panel);
  }
  .brand-band {
    position: absolute;
    left: 0; top: 244px;
    width: 507px; height: 219px;
    background: var(--band);
    display: flex;
    align-items: center;
    justify-content: center;
    gap: 16px;
  }
  .brand-dot {
    width: 46px; height: 46px;
    border-radius: 50%;
    background: var(--navy);
  }
  .brand-name {
    font-size: 40px;
    font-weight: 400;
    color: var(--navy);
    letter-spacing: 0.5px;
  }
  .doctor {
    position: absolute;
    left: 552px; top: 154px;
    width: 441px;
    color: var(--navy);
  }
  .doctor-name {
    font-size: 51px;
    line-height: 60px;
    white-space: nowrap;
  }
  .doctor-title {
    text-align: right;
    font-size: 29px;
    line-height: 30px;
    margin-top: -6px;
  }
  .contact-row {
    position: absolute;
    left: 554px;
    display: flex;
    align-items: flex-start;
    color: var(--blue);
  }
  .contact-row svg { flex: none; fill: var(--icon); }
  .contact-text {
    margin-left: 16px;
    font-size: 30px;
    line-height: 36px;
    white-space: nowrap;
  }
  .row-address { top: 302px; }
  .row-phone { top: 411px; }
  .row-fax { top: 500px; }
  .row-phone .contact-text, .row-fax .contact-text { color: var(--navy); }
</style>
</head>
<body>
<main class="card">
  <section class="brand-panel">
    <div class="brand-band">
      <span class="brand-dot"></span>
      <span class="brand-name">Brandwick Vue</span>
    </div>
  </section>

  <header class="doctor">
    <h1 class="doctor-name" style="font-weight:300">Loretta V Brandwick</h1>
    <p class="doctor-title">MD</p>
  </header>

  <div class="contact-row row-address">
    <svg width="45" height="45" viewBox="0 0 24 24" aria-hidden="true">
      <path d="M12 2 1 12h3v10h6v-6h4v6h6V12h3z"/>
    </svg>
    <p class="contact-text">4381 Fallow Crest Clinical Way Drive<br>Wilmington NC 28517</p>
  </div>

  <div class="contact-row row-phone">
    <svg width="46" height="46" viewBox="0 0 24 24" aria-hidden="true">
      <path d="M6.6 10.8c1.4 2.8 3.8 5.1 6.6 6.6l2.2-2.2c.3-.3.7-.4 1-.2 1.1.4 2.3.6 3.6.6.6 0 1 .4 1 1V20c0 .6-.4 1-1 1C10.6 21 3 13.4 3 4c0-.6.4-1 1-1h3.5c.6 0 1 .4 1 1 0 1.3.2 2.5.6 3.6.1.3 0 .7-.2 1z"/>
      <path d="M14 2.5a7.5 7.5 0 0 1 7.5 7.5h-1.6A5.9 5.9 0 0 0 14 4.1z"/>
      <path d="M14 6a4 4 0 0 1 4 4h-1.6A2.4 2.4 0 0 0 14 7.6z"/>
    </svg>
    <p class="contact-text" style="margin-top:5px">910.586.2741</p>
  </div>

  <div class="contact-row row-fax">
    <svg width="46" height="46" viewBox="0 0 24 24" aria-hidden="true">
      <rect x="6" y="2" width="12" height="4" rx="0.5"/>
      <path d="M3 7h18a1 1 0 0 1 1 1v8h-4v-3H6v3H2V8a1 1 0 0 1 1-1z"/>
      <path d="M7 14h10v8H10l-3-3z" fill="#ffffff" stroke="#555" stroke-width="0.6"/>
      <circle cx="19" cy="10" r="0.9" fill="#ffffff"/>
    </svg>
    <p class="contact-text" style="margin-top:5px">910.586.2799</p>
  </div>
</main>
</body>
</html>
```